Brindle Cove Needs a Website!

Single page (plus contact form) website for small home remodeling company. He's got a few pictures he'd like on the site and needs some basic text. He likes clean, simple designs and is "more traditional" in his stylistic preferences. Most of his business comes from word-of-mouth advertising and so the site is just something he needs for people to feel more comfortable with his business.

Target Market(s)

People who want to remodel their homes

Coding

Coded - Design and coding required

Number of Pages Required

2 page

Requirements
Must have
• Main page to include some or all of the attached images, contact page. Neutral colors. Old domain: brindlecoveabodes.com New domain: qm-holdings.com You can pull text from the old site or update it.
Should not have
• No loud colors/loud visual elements

```html
<!DOCTYPE html>
<html lang="en">
<head>
<meta charset="utf-8">
<title>Brindle Cove – Home Remodeling</title>
<link href="https://fonts.googleapis.com/css2?family=Montserrat:wght@300;400;500;600;700&display=swap" rel="stylesheet">
<style>
:root{
  --maroon:#3a120e;
  --orange:#e07b2a;
  --ink:#222;
  --muted:#666;
  --mist:#f6f6f6;
  --white:#fff;
}
*{box-sizing:border-box;margin:0;padding:0}
html,body{width:1200px;height:3158px;overflow:hidden;background:var(--white);font-family:'Montserrat',sans-serif;color:var(--ink)}
.page{position:absolute;left:88px;top:0;width:1024px;height:3158px}
.abs{position:absolute}
.btn{position:absolute;background:var(--orange);color:var(--white);font-size:10px;letter-spacing:.5px;text-transform:uppercase;display:flex;align-items:center;justify-content:center}
.rule{position:absolute;height:2px;background:var(--orange)}
.section-title{position:absolute;left:0;width:100%;text-align:center;font-size:27px;font-weight:600}

/* nav */
.nav{position:absolute;left:0;top:0;width:1024px;height:64px;background:var(--white)}
.brand-box{position:absolute;left:0;top:0;width:208px;height:54px;background:var(--maroon);display:flex;align-items:center;gap:14px;padding-left:26px;color:var(--white);font-weight:700;font-size:14px}
.brand-box i{width:16px;height:16px;border:2px solid var(--orange);display:block}
.menu{position:absolute;left:244px;top:22px;display:flex;gap:36px;font-size:11px}
.menu .active{color:var(--orange);border-bottom:1px solid var(--orange);padding-bottom:3px}
.socials{position:absolute;left:718px;top:21px;display:flex;gap:14px}
.socials span{width:13px;height:13px;border-radius:50%;border:1.5px solid var(--maroon);display:block}
.call{position:absolute;left:845px;top:0;width:180px;height:64px;background:var(--orange);color:var(--white);font-weight:700;text-align:center;font-size:12.5px;letter-spacing:1px;padding-top:13px;line-height:24px}

/* hero */
.hero{position:absolute;left:0;top:64px;width:1024px;height:505px;background:linear-gradient(135deg,#5a3a2c 0%,#7a5a48 45%,#4a2f24 100%)}
.hero h1{position:absolute;left:0;top:176px;width:100%;text-align:center;color:var(--white);font-size:49px;font-weight:700;line-height:56px}
.hero .btn{left:406px;top:342px;width:212px;height:41px;font-size:13px}

/* about */
.about-shadow{position:absolute;left:108px;top:700px;width:354px;height:237px;background:var(--maroon)}
.about-photo{position:absolute;left:84px;top:676px;width:362px;height:245px;background:linear-gradient(160deg,#d9c3a5,#8a6a55 60%,#3f5d6d)}
.about-title{position:absolute;left:514px;top:700px;font-size:27px;font-weight:600}
.about-text{position:absolute;left:514px;top:756px;width:410px;font-size:11.6px;line-height:20.2px;color:var(--muted);font-weight:300}

/* values */
.values{position:absolute;left:0;top:1042px;width:1024px;height:509px;background:var(--maroon);color:var(--white)}
.card{position:absolute;top:157px;width:224px;height:277px;background:var(--white);color:var(--ink);text-align:center}
.card .tag{position:absolute;left:-12px;top:12px;width:134px;height:40px;background:var(--orange);border-radius:0 20px 20px 20px;color:var(--white);font-size:11px;text-align:left;padding:12px 0 0 20px}
.card .icon{position:absolute;left:88px;top:72px;width:48px;height:48px;border:1.5px solid var(--orange);border-radius:6px;opacity:.7}
.card p{position:absolute;left:10px;top:140px;width:204px;font-size:11.5px;line-height:21px}
.card .more{position:absolute;left:24px;top:224px;font-size:10.5px;color:var(--orange)}
.card .corner{position:absolute;right:-10px;bottom:-4px}

/* blog */
.post{position:absolute;top:1727px;text-align:center}
.post .photo{height:176px}
.post .date{font-size:9px;margin-top:16px}
.post h3{font-size:13.5px;font-weight:500;margin-top:13px}
.post p{font-size:9.5px;line-height:12px;color:var(--muted);margin:12px auto 0;width:200px}
.post .read{font-size:9px;margin-top:30px;letter-spacing:.5px}

/* testimonials */
.testimonials{position:absolute;left:0;top:2200px;width:1024px;height:615px;background:var(--mist)}
.quote{position:absolute;top:134px;width:261px;height:342px;background:var(--white);box-shadow:0 2px 8px rgba(0,0,0,.12);text-align:center}
.quote .stars{color:var(--orange);font-size:19px;letter-spacing:3px;margin-top:32px}
.quote p{font-size:11.8px;line-height:18.6px;width:210px;margin:12px auto 0}
.quote .avatar{width:64px;height:64px;border-radius:50%;background:linear-gradient(160deg,#c9b9ad,#5a4f4a);margin:18px auto 0}
.quote .name{font-size:11px;margin-top:16px}
.quote .place{font-size:10px;color:var(--orange);margin-top:14px}

/* footer */
.footer{position:absolute;left:0;top:2815px;width:1024px;height:343px;background:var(--maroon);color:var(--white)}
.footer h4{font-weight:500;font-size:18px}
.footer ul{list-style:none;margin-top:16px}
.footer li{font-size:11.5px;line-height:20px;position:relative;padding-left:27px}
.footer li::before{content:"";position:absolute;left:0;top:8px;width:5px;height:5px;border-radius:50%;background:var(--orange)}
.footer .contact-row{display:flex;align-items:center;gap:20px;font-size:18px;margin-top:22px}
.footer .bar{position:absolute;left:54px;top:308px;width:920px;height:1px;background:rgba(255,255,255,.35)}
.footer .copy{position:absolute;left:0;top:318px;width:100%;text-align:center;font-size:12px}
</style>
</head>
<body>
<div class="page">

  <header class="nav">
    <div class="brand-box"><i></i>Brindle Cove</div>
    <nav class="menu">
      <span class="active">Home</span><span>Services</span><span>Projects</span><span>Blogs</span><span>About us</span><span>Contacts us</span>
    </nav>
    <div class="socials"><span></span><span></span><span></span><span></span></div>
    <div class="call">CALL US TODAY !<br>555-014-2290</div>
  </header>

  <section class="hero" role="img" aria-label="Warm living room interior with shelves, desk and windows">
    <h1>Welcome to&nbsp; Quentin Marsh<br>Enterprise</h1>
    <div class="btn">Make an appoinments</div>
  </section>

  <section class="about">
    <div class="about-shadow"></div>
    <div class="about-photo" role="img" aria-label="Remodeled open living room with staircase and kitchen"></div>
    <h2 class="about-title">ABOUT US</h2>
    <div class="rule" style="left:514px;top:738px;width:120px;height:1.5px"></div>
    <p class="about-text">When you want affordable, quality home construction services; think of us to do the job.<br>Since 1981 Quentin Marsh has built and remodeled over 400 homes and businesses. Let us be your contractor for the next project you start.<br>When quality, value and personal attention to detail are important With over 20 years experience in residential and commercial construction, you can trust your project to Brindle Cove Abodes</p>
    <div class="btn" style="left:514px;top:907px;width:121px;height:28px">Learn more</div>
  </section>

  <section class="values">
    <h2 class="section-title" style="top:36px;font-size:26px">DON'T TINKER AROUND</h2>
    <div class="abs" style="left:433px;top:82px;width:158px;height:1.5px;background:rgba(255,255,255,.8)"></div>

    <div class="card" style="left:81px">
      <div class="tag">PARTNERSHIP</div>
      <div class="icon" role="img" aria-label="Handshake line icon"></div>
      <p>I Have Built My Business With A Partnership Of Clients, Employees, Subcontractors</p>
      <div class="more">LEARN MORE</div>
      <svg class="corner" width="72" height="66" viewBox="0 0 72 66"><polygon points="72,0 72,66 0,66" fill="#e07b2a"/><text x="50" y="58" fill="#fff" font-family="Montserrat,sans-serif" font-size="22" font-weight="300">1</text></svg>
    </div>
    <div class="card" style="left:408px">
      <div class="tag">CONSTRUCTION</div>
      <div class="icon" role="img" aria-label="House with tools line icon"></div>
      <p>I Have Deep "Hands On" History In Construction From Foundations To Final Finishing Touches.</p>
      <div class="more">LEARN MORE</div>
      <svg class="corner" width="72" height="66" viewBox="0 0 72 66"><polygon points="72,0 72,66 0,66" fill="#e07b2a"/><text x="46" y="58" fill="#fff" font-family="Montserrat,sans-serif" font-size="22" font-weight="300">2</text></svg>
    </div>
    <div class="card" style="left:734px">
      <div class="tag">SUPPLIER</div>
      <div class="icon" role="img" aria-label="Delivery worker with boxes line icon"></div>
      <p>We Cultivate Suppliers Who Deliver Quality Materials On Time And Without Damage.</p>
      <div class="more">LEARN MORE</div>
      <svg class="corner" width="72" height="66" viewBox="0 0 72 66"><polygon points="72,0 72,66 0,66" fill="#e07b2a"/><text x="46" y="58" fill="#fff" font-family="Montserrat,sans-serif" font-size="22" font-weight="300">3</text></svg>
    </div>
  </section>

  <section class="blog">
    <h2 class="section-title" style="top:1626px;left:-6px">OUR BLOG</h2>
    <div class="abs" style="left:478px;top:1670px;width:56px;height:2px;background:var(--maroon)"></div>

    <article class="post" style="left:79px;width:234px">
      <div class="photo" role="img" aria-label="Bathroom with glass shower and tub" style="background:linear-gradient(160deg,#9aa3a6,#5c5652 60%,#3a302c)"></div>
      <div class="date">28 /09 /2020</div>
      <h3>Small Bathroom Ideas</h3>
      <p>sed ut perspiciatis, unde omnis iste natus error sit voluptatem accusantium doloremque laudantium, totam rem aperiam eaque ipsa, quae ab illo inventore veritatis et quasi architecto</p>
      <div class="read">READ&nbsp; FULL&nbsp; ARTICLE</div>
    </article>
    <article class="post" style="left:373px;width:256px">
      <div class="photo" role="img" aria-label="Open living room with staircase" style="background:linear-gradient(160deg,#d9c3a5,#8a6a55 60%,#3f5d6d)"></div>
      <div class="date">28 /09 /2020</div>
      <h3>Elegant Floating Vanities</h3>
      <p>sed ut perspiciatis, unde omnis iste natus error sit voluptatem accusantium doloremque laudantium, totam rem aperiam eaque ipsa, quae ab illo inventore veritatis et quasi architecto</p>
      <div class="read">READ&nbsp; FULL&nbsp; ARTICLE</div>
    </article>
    <article class="post" style="left:675px;width:259px">
      <div class="photo" role="img" aria-label="Kitchen with blue walls and steel fridge" style="background:linear-gradient(160deg,#2f4d7a,#6b5a4e 55%,#3a2a22)"></div>
      <div class="date">28 /09 /2020</div>
      <h3>Small Bathroom Ideas</h3>
      <p>sed ut perspiciatis, unde omnis iste natus error sit voluptatem accusantium doloremque laudantium, totam rem aperiam eaque ipsa, quae ab illo inventore veritatis et quasi architecto</p>
      <div class="read">READ&nbsp; FULL&nbsp; ARTICLE</div>
    </article>
    <div class="btn" style="left:445px;top:2111px;width:121px;height:28px">Learn more</div>
  </section>

  <section class="testimonials">
    <h2 class="section-title" style="top:40px">TESTIMONIAL</h2>
    <div class="rule" style="left:467px;top:84px;width:90px;height:1.5px"></div>

    <div class="quote" style="left:36px">
      <div class="stars">★★★★★</div>
      <p>lorem ipsum dolor sit amet, consectetur adipiscing elit. nulla sed cum nunc, egestas placerat vulputate id vitae. a id pellentesque suspendisse tortor mi elementum interdum mauris venenatis.</p>
      <div class="avatar" role="img" aria-label="Client portrait"></div>
      <div class="name">DANA WHITFIELD</div>
      <div class="place">SPRINGDALE.TN</div>
    </div>
    <div class="quote" style="left:370px">
      <div class="stars">★★★★★</div>
      <p>lorem ipsum dolor sit amet, consectetur adipiscing elit. nulla sed cum nunc, egestas placerat vulputate id vitae. a id pellentesque suspendisse tortor mi elementum interdum mauris venenatis.</p>
      <div class="avatar" role="img" aria-label="Client portrait"></div>
      <div class="name">DANA WHITFIELD</div>
      <div class="place">SPRINGDALE.TN</div>
    </div>
    <div class="quote" style="left:705px">
      <div class="stars">★★★★★</div>
      <p>lorem ipsum dolor sit amet, consectetur adipiscing elit. nulla sed cum nunc, egestas placerat vulputate id vitae. a id pellentesque suspendisse tortor mi elementum interdum mauris venenatis.</p>
      <div class="avatar" role="img" aria-label="Client portrait"></div>
      <div class="name">DANA WHITFIELD</div>
      <div class="place">SPRINGDALE.TN</div>
    </div>
    <div class="btn" style="left:451px;top:512px;width:121px;height:28px">Learn more</div>
  </section>

  <footer class="footer">
    <div class="abs" style="left:54px;top:82px;width:210px">
      <h4 style="font-size:24px">Brindle Cove</h4>
      <p style="font-size:11.5px;line-height:19px;margin-top:18px">Since 1981 Quentin Marsh has built and remodeled over 400 homes and businesses. Let us be your contractor for the next project you start.</p>
      <div class="socials" style="position:static;display:flex;gap:30px;margin-top:22px;padding-left:16px"><span style="border-color:#fff"></span><span style="border-color:#fff"></span><span style="border-color:#fff"></span><span style="border-color:#fff"></span></div>
    </div>
    <div class="abs" style="left:308px;top:90px">
      <h4>SERVICE</h4>
      <ul><li>Addition</li><li>New Construction</li><li>historic renovations</li><li>painting</li><li>gutters</li><li>electric</li></ul>
    </div>
    <div class="abs" style="left:510px;top:86px">
      <h4>CUSTOMER CARE</h4>
      <ul style="margin-top:14px"><li style="line-height:26px">About Us</li><li style="line-height:26px">Our Services</li><li style="line-height:26px">blog</li><li style="line-height:26px">Contact Us</li><li style="line-height:26px">Contact Us</li></ul>
    </div>
    <div class="abs" style="left:733px;top:82px">
      <h4 style="font-size:20px;font-weight:400">Call Now For Services!</h4>
      <div style="color:var(--orange);font-size:20px;margin-top:6px">555-014-2290</div>
      <div class="contact-row" style="margin-top:28px">
        <svg width="18" height="14" viewBox="0 0 18 14" fill="none" stroke="#fff" stroke-width="1.3"><rect x="1" y="1" width="16" height="12"/><path d="M1 1l8 7 8-7"/></svg>Email Us</div>
      <div class="contact-row">
        <svg width="18" height="20" viewBox="0 0 18 20" fill="none" stroke="#fff" stroke-width="1.3"><path d="M9 19s7-6.5 7-11A7 7 0 0 0 2 8c0 4.5 7 11 7 11z"/><circle cx="9" cy="8" r="2.5"/></svg>Get Direction</div>
    </div>
    <div class="bar"></div>
    <div class="copy">Brindle Cove © 2021 All Rights Reserved. Terms of Use and Privacy Policy</div>
  </footer>

</div>
</body>
</html>
```